Property Service business needs a cool business card

Looking for an eloquent and unique business card using the logo and colours attached as uploaded files.

Target Market(s)

Body corporates, real estate agents, building managers

Industry/Entity Type

Business

Contact Information for Business Card

- Kelvo Logo
- Construction * Maintenance * Remedial

- Ned Pirrick
- Business Manager

- Ph 0417586043
- P.O Box 514 South Melbourne Vic 3090
- Email ned@kelvo.com
- Website www.kelvopropertyservices.com.au

Requirements
Must have
• Clean and fresh look, colours must be vibrant!
Nice to have
• unique features
Should not have
• Should not be overcrowded

```html
<!DOCTYPE html>
<html lang="en">
<head>
<meta charset="utf-8">
<title>Kelvo Property Services – Business Card</title>
<link rel="stylesheet" href="https://fonts.googleapis.com/css2?family=Open+Sans:wght@400;600&display=swap">
<style>
  :root {
    --brand-blue: #1a4c9c;
    --line-blue: #3f7fd0;
    --brand-green: #8dc21f;
    --ink: #2b2b2b;
    --muted: #555a60;
    --paper: #ffffff;
    --backdrop: #eceef1;
  }
  * { box-sizing: border-box; margin: 0; padding: 0; }
  html, body { width: 1200px; height: 900px; overflow: hidden; }
  body {
    background: var(--backdrop);
    font-family: "Open Sans", Arial, sans-serif;
    display: flex;
    flex-direction: column;
    align-items: center;
    justify-content: center;
    gap: 44px;
  }
  .card {
    position: relative;
    width: 640px;
    height: 366px;
    overflow: hidden;
    box-shadow: 0 6px 18px rgba(0,0,0,0.15);
  }

  /* Back side */
  .card--back { background: var(--brand-blue); }
  .card--back .wordmark {
    position: absolute;
    left: 228px; top: 132px;
    display: flex; align-items: center; gap: 14px;
    color: var(--paper);
    font-weight: 400;
    font-size: 52px;
    letter-spacing: 1px;
  }
  .mark-square {
    display: inline-block;
    width: 40px; height: 40px;
    background: var(--brand-green);
  }
  .card--back .rule {
    position: absolute;
    height: 1px;
    background: var(--line-blue);
  }
  .rule--upper { left: 430px; right: 0; top: 150px; }
  .rule--lower { left: 0; width: 180px; top: 262px; }
  .card--back .website {
    position: absolute;
    left: 190px; top: 250px;
    color: var(--paper);
    font-size: 15px;
    letter-spacing: 0.3px;
  }

  /* Front side */
  .card--front { background: var(--paper); }
  .card--front .band { position: absolute; inset: 0; }
  .card--front .wordmark {
    position: absolute;
    left: 52px; top: 150px;
    display: flex; align-items: center; gap: 12px;
    color: var(--brand-blue);
    font-weight: 400;
    font-size: 44px;
    letter-spacing: 1px;
  }
  .card--front .wordmark .mark-square { width: 34px; height: 34px; }
  .services {
    position: absolute;
    left: 22px; top: 268px;
    color: var(--brand-blue);
    font-size: 12px;
    letter-spacing: 0.4px;
  }
  .divider {
    position: absolute;
    left: 352px; top: 22px;
    width: 1px; height: 190px;
    background: #d5d8dc;
  }
  .person {
    position: absolute;
    left: 374px; top: 36px;
  }
  .person .name {
    color: var(--ink);
    font-size: 19px;
    letter-spacing: 0.5px;
    text-transform: uppercase;
  }
  .person .role {
    color: var(--brand-green);
    font-size: 13px;
    margin-top: 2px;
  }
  .contacts {
    position: absolute;
    left: 374px; top: 130px;
    list-style: none;
    color: var(--muted);
    font-size: 12px;
  }
  .contacts li { display: flex; align-items: center; gap: 10px; margin-bottom: 7px; }
  .contacts svg { width: 12px; height: 12px; flex: none; }
  .web-link {
    position: absolute;
    right: 20px; top: 314px;
    display: flex; align-items: center; gap: 8px;
    color: var(--paper);
    font-size: 13px;
    font-weight: 600;
    white-space: nowrap;
  }
  .web-link svg { width: 13px; height: 13px; }
</style>
</head>
<body>

  <section class="card card--back" aria-label="Card back">
    <div class="rule rule--upper"></div>
    <div class="wordmark"><span class="mark-square"></span>Kelvo</div>
    <div class="rule rule--lower"></div>
    <p class="website">www.kelvopropertyservices.com.au</p>
  </section>

  <section class="card card--front" aria-label="Card front">
    <svg class="band" viewBox="0 0 640 366" preserveAspectRatio="none" aria-hidden="true">
      <path d="M0 318 L300 318 C335 318 345 286 380 286 L640 286 L640 296 L386 296 C352 296 342 328 306 328 L0 328 Z" fill="var(--brand-green)"/>
      <path d="M0 332 L312 332 C346 332 358 300 392 300 L640 300 L640 366 L0 366 Z" fill="var(--brand-blue)"/>
    </svg>

    <div class="wordmark"><span class="mark-square"></span>Kelvo</div>
    <p class="services">CONSTRUCTION | MAINTENANCE | REMEDIAL</p>

    <div class="divider"></div>
    <div class="person">
      <p class="name">Ned Pirrick</p>
      <p class="role">Business Manager</p>
    </div>

    <ul class="contacts">
      <li>
        <svg viewBox="0 0 12 12"><path d="M6 0.5a4 4 0 0 0-4 4c0 3 4 7 4 7s4-4 4-7a4 4 0 0 0-4-4zm0 5.6a1.6 1.6 0 1 1 0-3.2 1.6 1.6 0 0 1 0 3.2z" fill="var(--brand-green)"/></svg>
        P.O Box 514 South Melbourne Vic 3090
      </li>
      <li>
        <svg viewBox="0 0 12 12"><path d="M2.4 0.8l2 2.2-1 1.4c.6 1.6 1.8 2.8 3.4 3.4l1.4-1 2.2 2-1.2 2C5 10.6 1.4 7 .4 2z" fill="var(--brand-green)"/></svg>
        0417586043
      </li>
      <li>
        <svg viewBox="0 0 12 12"><rect x="0.5" y="2" width="11" height="8" fill="var(--brand-green)"/><path d="M0.5 2.4 6 6.6l5.5-4.2" stroke="#fff" stroke-width="1" fill="none"/></svg>
        ned@kelvo.com
      </li>
    </ul>

    <p class="web-link">
      <svg viewBox="0 0 14 14"><circle cx="7" cy="7" r="6" fill="none" stroke="#fff" stroke-width="1.3"/><path d="M1 7h12M7 1c-2.4 2.6-2.4 9.4 0 12M7 1c2.4 2.6 2.4 9.4 0 12" stroke="#fff" stroke-width="1" fill="none"/></svg>
      www.kelvopropertyservices.com.au
    </p>
  </section>

</body>
</html>
```